Pella Acupuncture Business Card Design

I would like a business card design for my acupuncture business which is based from 2 practices in Melbourne, Australia.

The front of the card should include:

*The Logo
* Name - Miranda Tovelisca (B.Hlth.Sc.(EM), Dip.Cl.Mass.). (I would like the letters after my name in slightly smaller font)
* Mobile number - 0472 318 604
* Web address - www.pellaacupuncture-example.com.au

On the back of the card I would somehow like to fit my 2 clinic addresses in. They are:

The Birchwood Restoration Rooms
842 Fennimore Rd, Larkhaven VIC 3187
Ph: 1300 274 518

Quillbrook Integrative & Eastern Herbal Therapy Clinic
31 Marlowby Rd, Tessendale East VIC 3192
Ph: (03) 9871 3352

If there is space, I'd also like to add to the back of the card - Next Appointment............................ (or something along those lines).

Thanks and happy designing!

Target Market(s)

Health consumers, and colleagues in the health industry

Industry/Entity Type

Clinic

Contact Information for Business Card

as above in brief

Requirements
Must have
• I've seen some ok designs coming in, however I'd like to avoid the generic look with the added curved line details etc. I don't particularly need extra patterns added to the card. I'd prefer it to look quite clean and simple, and using more earthy colours (I'm not super keen on the lime green that a lot of designs seem to include. I don't mind the full black or white look, (obviously the back side needs to be a lighter colour to allow me to write appointment details on it). I also quite like the idea of the background looking like brown recycled paper (just an idea - that's not 100% necessary).
Nice to have
• I have an idea that I could have the main flower part of the logo printed as metallic.
Should not have
• Generic patterns and too much added detail.

```html
<!DOCTYPE html>
<html lang="en">
<head>
<meta charset="utf-8">
<title>Pella Acupuncture Business Card</title>
<link href="https://fonts.googleapis.com/css2?family=Open+Sans:wght@400;600;700&display=swap" rel="stylesheet">
<style>
  :root {
    --backdrop: #e7e2da;
    --paper-light: #f3ede2;
    --paper-mid: #e6dccb;
    --paper-edge: #d3c6b0;
    --ink: #262424;
    --ink-soft: #4a4745;
    --leaf-green: #3fae3a;
    --mark-dark: #1f1f1f;
    --mark-light: #f1ecdf;
  }
  * { box-sizing: border-box; margin: 0; padding: 0; }
  html, body {
    width: 1200px; height: 1023px; overflow: hidden;
    background: var(--backdrop);
    font-family: "Open Sans", Arial, sans-serif;
    color: var(--ink);
  }
  .canvas { position: relative; width: 1200px; height: 1023px; }
  .card {
    position: absolute; left: 250px; width: 700px; height: 400px;
    background: radial-gradient(ellipse at 40% 35%, var(--paper-light) 0%, var(--paper-mid) 75%, var(--paper-edge) 100%);
    box-shadow: 0 6px 18px rgba(60, 45, 25, 0.25);
    overflow: hidden;
  }
  .card--front { top: 70px; }
  .card--back { top: 550px; }

  /* front */
  .brand {
    position: absolute; left: 90px; top: 50px;
    display: flex; align-items: center; gap: 18px;
  }
  .brand__dot {
    width: 60px; height: 60px; border-radius: 50%;
    background: var(--mark-dark);
  }
  .brand__name {
    font-size: 30px; font-weight: 600; color: var(--ink);
    letter-spacing: 1px;
  }
  .identity {
    position: absolute; left: 60px; top: 250px;
    display: flex; align-items: baseline; gap: 10px;
  }
  .identity__name { font-size: 30px; font-weight: 700; color: var(--ink); }
  .identity__divider { font-size: 30px; font-weight: 400; color: var(--ink); }
  .identity__credentials { font-size: 15px; color: var(--ink-soft); }
  .contact {
    position: absolute; left: 378px; top: 300px;
    list-style: none; font-size: 15px; color: var(--ink-soft); line-height: 30px;
  }
  .contact__item { display: flex; align-items: center; gap: 8px; }
  .contact__icon { width: 14px; height: 14px; flex: none; }

  /* back */
  .appointment {
    position: absolute; left: 50px; top: 40px;
    font-size: 20px; font-weight: 700; color: var(--ink); line-height: 30px;
  }
  .appointment__line { display: flex; align-items: baseline; }
  .appointment__rule {
    display: inline-block; width: 260px; margin-left: 6px;
    border-bottom: 2px dotted var(--ink);
  }
  .clinic { position: absolute; left: 50px; font-size: 15px; line-height: 22px; color: var(--ink-soft); }
  .clinic--one { top: 170px; }
  .clinic--two { top: 265px; }
  .clinic__name { font-size: 17px; font-weight: 700; color: var(--leaf-green); }
  .back-brand {
    position: absolute; right: 0; top: 0; width: 130px; height: 400px;
    background: var(--mark-dark);
    display: flex; align-items: center; justify-content: center;
  }
  .back-brand__name {
    writing-mode: vertical-rl;
    font-size: 20px; font-weight: 600; color: var(--mark-light); letter-spacing: 1px;
  }
</style>
</head>
<body>
<main class="canvas">
  <section class="card card--front" aria-label="Card front">
    <div class="brand">
      <span class="brand__dot"></span>
      <span class="brand__name">Pella Acupuncture</span>
    </div>
    <div class="identity">
      <span class="identity__name">Miranda Tovelisca</span>
      <span class="identity__divider">/</span>
      <span class="identity__credentials">(B.Hlth.Sc.(EM), Dip.Cl.Mass.)</span>
    </div>
    <ul class="contact">
      <li class="contact__item">
        <svg class="contact__icon" viewBox="0 0 14 14"><rect x="3" y="0.5" width="8" height="13" rx="1.5" fill="none" stroke="#4a4745" stroke-width="1.4"/><circle cx="7" cy="11" r="0.9" fill="#4a4745"/></svg>
        0472 318 604
      </li>
      <li class="contact__item">
        <svg class="contact__icon" viewBox="0 0 14 14"><circle cx="7" cy="7" r="6" fill="none" stroke="#4a4745" stroke-width="1.3"/><path d="M1 7h12M7 1c-3 3.5-3 8.5 0 12M7 1c3 3.5 3 8.5 0 12" fill="none" stroke="#4a4745" stroke-width="1"/></svg>
        www.pellaacupuncture-example.com.au
      </li>
    </ul>
  </section>

  <section class="card card--back" aria-label="Card back">
    <div class="appointment">
      <p>Next Appointment:</p>
      <p class="appointment__line">Date:<span class="appointment__rule"></span></p>
      <p class="appointment__line">Time:<span class="appointment__rule"></span></p>
    </div>
    <div class="clinic clinic--one">
      <p class="clinic__name">The Birchwood Restoration Rooms</p>
      <p>842 Fennimore Rd, Larkhaven VIC 3187</p>
      <p>Ph: 1300 274 518</p>
    </div>
    <div class="clinic clinic--two">
      <p class="clinic__name">Quillbrook Integrative &amp; Eastern Herbal Therapy Clinic</p>
      <p>31 Marlowby Rd, Tessendale East VIC 3192</p>
      <p>Ph: (03) 9871 3352</p>
    </div>
    <div class="back-brand">
      <span class="back-brand__name">Pella Acupuncture</span>
    </div>
  </section>
</main>
</body>
</html>
```